Start up needs juice bottle label design

Tarbeck Sunvale juice company needs juice bottle label design for all natural lemonades, teas, smoothies and cold-pressed juice. We would like the design to have a space for multiple flavors or custom recipes for special orders. Below is the company logo.

Target Market(s)

On-the-go Health conscious

```html
<!DOCTYPE html>
<html lang="en">
<head>
<meta charset="utf-8">
<title>Tarbeck Sunvale – Apple Juice Label</title>
<link rel="stylesheet" href="https://fonts.googleapis.com/css2?family=Oswald:wght@600;700&family=Roboto+Slab:wght@500;700&display=swap">
<style>
  :root {
    --backdrop: #ececec;
    --label-cream: #fdf8ea;
    --fruit-warm: #f6c75a;
    --fruit-pink: #f08a9a;
    --fruit-blue: #7cc4e0;
    --band-yellow: #f7d51e;
    --ink-dark: #2a2522;
    --brand-blue: #2f6fc9;
  }
  * { margin: 0; padding: 0; box-sizing: border-box; }
  html, body {
    width: 820px;
    height: 1200px;
    overflow: hidden;
    background: var(--backdrop);
  }
  .canvas {
    width: 820px;
    height: 1200px;
    display: flex;
    align-items: center;
    justify-content: center;
  }
  .label {
    width: 600px;
    height: 1080px;
    background: var(--label-cream);
    position: relative;
    display: flex;
    flex-direction: column;
    align-items: center;
    overflow: hidden;
  }
  .fruit-art {
    width: 100%;
    flex: none;
  }
  .fruit-art--top {
    height: 250px;
    background: linear-gradient(135deg, var(--fruit-warm) 0%, #f9e3a8 35%, var(--fruit-pink) 65%, #f9d9c4 85%, var(--fruit-blue) 100%);
    opacity: 0.85;
  }
  .fruit-art--bottom {
    height: 300px;
    margin-top: auto;
    background: linear-gradient(315deg, var(--fruit-warm) 0%, #f9e3a8 30%, var(--fruit-pink) 55%, #f9d9c4 80%, var(--fruit-blue) 100%);
    opacity: 0.85;
  }
  .brand-name {
    margin-top: 24px;
    font-family: "Oswald", sans-serif;
    font-weight: 700;
    font-size: 58px;
    line-height: 1;
    letter-spacing: 1px;
    color: var(--brand-blue);
    text-align: center;
  }
  .flavor-band {
    margin-top: 34px;
    width: 380px;
    padding: 14px 0 12px;
    background: var(--band-yellow);
    border-radius: 0 40px 0 40px;
    text-align: center;
  }
  .flavor-name {
    font-family: "Oswald", sans-serif;
    font-weight: 700;
    font-size: 56px;
    line-height: 1.02;
    color: var(--ink-dark);
    text-transform: uppercase;
  }
  .claim {
    margin-top: 18px;
    font-family: "Roboto Slab", serif;
    font-weight: 700;
    font-size: 30px;
    letter-spacing: 1px;
    color: var(--ink-dark);
  }
  .ingredients {
    margin-top: 20px;
    font-family: "Roboto Slab", serif;
    font-weight: 500;
    font-size: 22px;
    line-height: 1.3;
    color: var(--ink-dark);
    text-align: center;
  }
  .volume {
    margin-top: 18px;
    margin-bottom: 20px;
    font-family: "Roboto Slab", serif;
    font-weight: 500;
    font-size: 22px;
    color: var(--ink-dark);
  }
</style>
</head>
<body>
<main class="canvas">
  <section class="label">
    <div class="fruit-art fruit-art--top" role="img" aria-label="Illustrated pattern of lemons, strawberries, watermelon slices, dragon fruit and leaves"></div>

    <h1 class="brand-name">Tarbeck Sunvale</h1>

    <div class="flavor-band">
      <h2 class="flavor-name">Apple<br>Juice</h2>
    </div>

    <p class="claim">100% NATURAL</p>

    <p class="ingredients">Ingredients:<br>Fresh apple, water,<br>apple pure, sugar.</p>

    <p class="volume">250 ml</p>

    <div class="fruit-art fruit-art--bottom" role="img" aria-label="Illustrated pattern of apples, cherries, bananas, lemons, strawberries, watermelon and dragon fruit"></div>
  </section>
</main>
</body>
</html>
```